"Fern Hollow Realty" is the name of my real estate company

This is for a: "for sale" sign, looking for a minimalist design, wire frame outline of a midcentury modern homes roof line or elevation?

My name is: Derek Malloy (needed)
My Cell # is: 555 204 3967 (needed)
My BRE license # is: 04827265 (needed)
BRE needs to be displayed in this format: BRE 04827265 (needed)
The white outline on the sign riders 'pictured" may work on large sign
Note font on pictured rider sign

This design is for a real estate "for sale" sign or sandwich board sign. Do Not include the words "For Sale" on the sign.

The measurements are 36" inches (91.44 cm) Length, or tall X 24" inches (60.90 cm) Wide.

|
3
---- 24 ----
6
|

Sorry I wasn't more specific earlier. I'd like the elements of the sign to be scaled in size according to their importance, from largest to smallest:

My name: Derek Malloy
My phone number: 555-204-3967
My company name: Fern Hollow Realty
My license number: BRE 04827265 (This can be much smaller than the smallest text)
Additionally, please incorporate contemporary to mid-century modern elements on the wire frame roofline or a simple roof-like design.

Thank you!

Best regards,
Derek

```html
<!DOCTYPE html>
<html lang="en">
<head>
<meta charset="UTF-8">
<title>Fern Hollow Realty — Derek Malloy Sign</title>
<link rel="stylesheet" href="https://fonts.googleapis.com/css2?family=Montserrat:wght@400;600&display=swap">
<style>
  :root {
    --sign-black: #000000;
    --sign-white: #ffffff;
    --roofline-tone: #2a2a2a;
  }
  html, body {
    margin: 0;
    padding: 0;
    width: 1200px;
    height: 1200px;
    overflow: hidden;
    background: var(--sign-black);
  }
  .canvas {
    position: relative;
    width: 1200px;
    height: 1200px;
    background: var(--sign-black);
    font-family: "Montserrat", sans-serif;
    color: var(--sign-white);
  }
  .sign {
    position: absolute;
    left: 260px;
    top: 90px;
    width: 680px;
    height: 1020px;
    box-sizing: border-box;
    border: 7px solid var(--sign-white);
  }
  .sign > * {
    position: absolute;
    left: 0;
    right: 0;
    margin: 0;
    text-align: center;
    line-height: 1;
    text-transform: uppercase;
  }
  .company-name {
    top: 100px;
    font-size: 33px;
    font-weight: 400;
    letter-spacing: 0.2em;
  }
  .roofline-art {
    left: 199px;
    right: auto;
    top: 305px;
    width: 268px;
    height: 126px;
  }
  .agent-name {
    top: 520px;
    font-size: 78px;
    font-weight: 400;
    letter-spacing: 0.01em;
  }
  .name-rule {
    left: 256px;
    right: auto;
    top: 617px;
    width: 154px;
    height: 6px;
    background: var(--sign-white);
  }
  .agent-phone {
    top: 648px;
    font-size: 48px;
    font-weight: 400;
    letter-spacing: 0.08em;
  }
  .license-number {
    top: 946px;
    font-size: 16px;
    font-weight: 600;
    letter-spacing: 0.07em;
  }
</style>
</head>
<body>
  <main class="canvas">
    <section class="sign">
      <p class="company-name">Fern Hollow Realty</p>
      <svg class="roofline-art" role="img" aria-label="Wireframe outline of a mid-century modern house roofline and elevation" viewBox="0 0 268 126">
        <rect width="268" height="126" fill="var(--roofline-tone)"/>
      </svg>
      <h1 class="agent-name">Derek Malloy</h1>
      <div class="name-rule"></div>
      <p class="agent-phone">555-204-3967</p>
      <p class="license-number">License Number: BRE 04827265</p>
    </section>
  </main>
</body>
</html>
```